Menu Design Project

We are a cafe in italy our name is "Bright Corvella Cafe & Food"

We need a new menu we offer cafes and snacks.

our web site is brightcorvella.com you can find there our logo.

We need something clean to print so we can offer to our clients a good menu.

Target Market(s)

cafe clients

Industry/Entity Type

Cafe

Requirements
Must have
• - Nice design
- Our logo
- Demo text so we can write our text

```html
<!DOCTYPE html>
<html lang="en">
<head>
<meta charset="utf-8">
<title>Bright Corvella Cafe &amp; Food — Menu</title>
<link rel="stylesheet" href="https://fonts.googleapis.com/css2?family=Roboto+Slab:wght@400;700;800&display=swap">
<style>
  :root{
    --canvas:#ffffff;
    --frame:#000000;
    --paper:#1c1f27;
    --paper-deep:#14161c;
    --gold:#e3a547;
    --gold-light:#f4c87a;
    --ink:#ffffff;
    --ink-soft:#d9d9de;
    --slab:"Roboto Slab", Georgia, serif;
  }
  *{box-sizing:border-box;margin:0;padding:0}
  html,body{width:1200px;height:1200px;overflow:hidden;background:var(--canvas)}
  .canvas{position:relative;width:1200px;height:1200px;font-family:var(--slab);color:var(--ink)}

  .page{position:absolute;background:var(--paper);border:12px solid var(--frame);overflow:hidden;
    background-image:repeating-linear-gradient(45deg,rgba(255,255,255,.025) 0 2px,transparent 2px 5px),
                     repeating-linear-gradient(-45deg,rgba(0,0,0,.18) 0 2px,transparent 2px 5px);}
  .page--vegetables{left:12px;top:10px;width:462px;height:734px}
  .page--drinks{left:572px;top:24px;width:476px;height:734px}
  .page--meals{left:74px;top:414px;width:476px;height:732px}
  .page--cover{left:692px;top:408px;width:474px;height:732px}

  .photo{position:absolute}
  .photo--cream{background:linear-gradient(135deg,#f1ece4,#b89f86 55%,#3b2619)}
  .photo--berry{background:linear-gradient(120deg,#b5c46a,#f4eee6 45%,#c8372f 75%,#7c5336)}
  .photo--beans{background:radial-gradient(circle at 40% 40%,#6b3a22,#2a140b 70%)}
  .photo--salad{background:linear-gradient(135deg,#e7c9a3,#5f8a3a 40%,#cf4b2e 70%,#3f2a1e)}
  .photo--pasta{background:linear-gradient(135deg,#6f8f4a,#b9865a 40%,#d89a6a 70%,#eae2d6)}
  .photo--platter{background:linear-gradient(120deg,#c9584e,#e39b85 35%,#d8a441 65%,#efe3c6)}

  .feature{position:absolute;width:104px;border:3px solid var(--gold);
    background:linear-gradient(180deg,#2a2d35,#0c0d10);padding:9px 7px 8px;text-align:center}
  .feature__title{font-weight:700;font-size:13px;line-height:1.15;margin-bottom:6px}
  .feature__text{font-size:5.6px;line-height:1.45;color:var(--ink-soft);font-weight:700}

  .section{position:absolute}
  .section__head{display:flex;align-items:center;gap:9px;height:20px}
  .marker{display:block;width:14px;height:14px;border:3px solid var(--gold);flex:none}
  .section__title{font-weight:700;font-size:15px;letter-spacing:.2px;white-space:nowrap}
  .items{position:absolute;left:0}
  .item{height:29px;width:125px}
  .item__name{font-weight:700;font-size:9.4px;line-height:12px;white-space:nowrap}
  .item__desc{display:flex;align-items:baseline;font-size:6.2px;font-weight:700;color:var(--ink-soft);line-height:9px;white-space:nowrap}
  .item__dots{flex:1;border-bottom:1px dotted var(--ink-soft);margin:0 2px;transform:translateY(-2px)}

  .badge{position:absolute;width:17px;height:17px;border-radius:50%;border:1.5px solid var(--ink);
    display:flex;align-items:center;justify-content:center}
  .badge svg{width:10px;height:10px;fill:var(--ink)}

  .brand{position:absolute;left:185px;top:50px;width:103px;height:103px;border:3px solid var(--gold);
    background:#07080a;display:flex;align-items:center;justify-content:center;text-align:center}
  .brand__name{font-weight:700;font-size:13px;line-height:1.15;color:var(--gold)}
  .welcome{position:absolute;left:30px;right:30px;top:200px;text-align:center;font-weight:700;font-size:14px;line-height:19px}
  .thumb{position:absolute;top:292px;width:100px;height:100px;border:3px solid var(--gold)}
  .thumb__fill{width:100%;height:100%}
  .fill--pasta{background:linear-gradient(135deg,#d9c17a,#6a8b3c 50%,#c24a2c)}
  .fill--grill{background:radial-gradient(circle at 45% 45%,#7a4530,#2b140c 75%)}
  .fill--chicken{background:radial-gradient(circle at 50% 50%,#a04a26,#4a1d0d 70%,#7a6a5a)}
  .page--cover .item{width:120px}

  .cover__footer{position:absolute;left:0;right:0;bottom:0;height:156px;background:#000}
  .symbols__head{position:absolute;left:0;right:0;top:10px;text-align:center}
  .symbols__head .marker{margin:0 auto 4px}
  .symbols__title{font-weight:700;font-size:13px}
  .symbols__sub{font-size:5.6px;font-weight:700}
  .symbol{position:absolute;top:64px;width:52px;text-align:center;transform:translateX(-50%)}
  .symbol .badge{position:relative;margin:0 auto 5px;width:22px;height:22px;border:none;background:var(--ink)}
  .symbol .badge svg{fill:#000;width:13px;height:13px}
  .symbol__name{font-size:5.6px;font-weight:700;line-height:8px}
  .symbol__text{font-size:5px;line-height:7px;color:var(--ink-soft)}
</style>
</head>
<body>
<svg width="0" height="0" style="position:absolute" aria-hidden="true">
  <symbol id="i-star" viewBox="0 0 10 10"><path d="M5 0l1.5 3.3 3.5.4-2.6 2.4.7 3.5L5 7.8 1.9 9.6l.7-3.5L0 3.7l3.5-.4z"/></symbol>
  <symbol id="i-flame" viewBox="0 0 10 10"><path d="M5 0c1 2 3 3 3 6a3 3 0 0 1-6 0c0-1.5 1-2.5 1.5-3.5C4 4 4.5 4.5 5 4c.3-1.5 0-3 0-4z"/></symbol>
  <symbol id="i-flower" viewBox="0 0 10 10"><circle cx="5" cy="2" r="2"/><circle cx="8" cy="5" r="2"/><circle cx="5" cy="8" r="2"/><circle cx="2" cy="5" r="2"/></symbol>
  <symbol id="i-leaf" viewBox="0 0 10 10"><path d="M2 10C2 4 5 1 9 0 9 5 6 8 3 8z"/></symbol>
  <symbol id="i-zero" viewBox="0 0 10 10"><text x="5" y="7.2" font-size="6" text-anchor="middle" font-family="Arial, sans-serif" font-weight="700">0%</text></symbol>
  <symbol id="i-moon" viewBox="0 0 10 10"><path d="M6 0a5 5 0 1 0 4 7A4 4 0 0 1 6 0z"/></symbol>
  <symbol id="i-kid" viewBox="0 0 10 10"><circle cx="5" cy="5" r="4"/><circle cx="2" cy="1.8" r="1.4"/><circle cx="8" cy="1.8" r="1.4"/></symbol>
</svg>

<main class="canvas">

  <!-- Page: vegetables & pies -->
  <section class="page page--vegetables">
    <div class="photo photo--cream" style="left:246px;top:2px;width:204px;height:226px" role="img" aria-label="Photo of layered cream desserts in glasses with coffee beans"></div>
    <div class="photo photo--berry" style="left:246px;top:234px;width:204px;height:200px" role="img" aria-label="Photo of a creamy pie slice topped with strawberries"></div>

    <div class="section" style="left:19px;top:26px">
      <div class="section__head"><span class="section__title">Fresh Vegetables</span><span class="marker" style="margin-left:2px"></span></div>
    </div>
    <div class="items" style="left:19px;top:52px">
      <div class="item"><div class="item__name">Name of the article</div><div class="item__desc">Description of the article<span class="item__dots"></span>00.00</div></div>
      <div class="item"><div class="item__name">Name of the article</div><div class="item__desc">Description of the article<span class="item__dots"></span>00.00</div></div>
      <div class="item"><div class="item__name">Name of the article</div><div class="item__desc">Description of the article<span class="item__dots"></span>00.00</div></div>
      <div class="item"><div class="item__name">Name of the article</div><div class="item__desc">Description of the article<span class="item__dots"></span>00.00</div></div>
      <div class="item"><div class="item__name">Name of the article</div><div class="item__desc">Description of the article<span class="item__dots"></span>00.00</div></div>
      <div class="item"><div class="item__name">Name of the article</div><div class="item__desc">Description of the article<span class="item__dots"></span>00.00</div></div>
    </div>
    <span class="badge" style="left:160px;top:108px"><svg><use href="#i-star"/></svg></span>

    <div class="section" style="left:19px;top:248px">
      <div class="section__head"><span class="section__title">Special pies</span><span class="marker" style="margin-left:38px"></span></div>
    </div>
    <div class="items" style="left:19px;top:274px">
      <div class="item"><div class="item__name">Name of the article</div><div class="item__desc">Description of the article<span class="item__dots"></span>00.00</div></div>
      <div class="item"><div class="item__name">Name of the article</div><div class="item__desc">Description of the article<span class="item__dots"></span>00.00</div></div>
      <div class="item"><div class="item__name">Name of the article</div><div class="item__desc">Description of the article<span class="item__dots"></span>00.00</div></div>
      <div class="item"><div class="item__name">Name of the article</div><div class="item__desc">Description of the article<span class="item__dots"></span>00.00</div></div>
      <div class="item"><div class="item__name">Name of the article</div><div class="item__desc">Description of the article<span class="item__dots"></span>00.00</div></div>
      <div class="item"><div class="item__name">Name of the article</div><div class="item__desc">Description of the article<span class="item__dots"></span>00.00</div></div>
      <div class="item"><div class="item__name">Name of the article</div><div class="item__desc">Description of the article<span class="item__dots"></span>00.00</div></div>
    </div>
    <span class="badge" style="left:160px;top:271px"><svg><use href="#i-star"/></svg></span>
    <span class="badge" style="left:160px;top:300px"><svg><use href="#i-leaf"/></svg></span>

    <div class="section" style="left:19px;top:514px">
      <div class="section__head"><span class="section__title">General</span></div>
    </div>
    <div class="items" style="left:19px;top:560px">
      <div class="item"><div class="item__name">Name of the article</div><div class="item__desc">Description of the article<span class="item__dots"></span>00.00</div></div>
      <div class="item"><div class="item__name">Name of the article</div><div class="item__desc">Description of the article<span class="item__dots"></span>00.00</div></div>
      <div class="item"><div class="item__name">Name of the article</div><div class="item__desc">Description of the article<span class="item__dots"></span>00.00</div></div>
      <div class="item"><div class="item__name">Name of the article</div><div class="item__desc">Description of the article<span class="item__dots"></span>00.00</div></div>
      <div class="item"><div class="item__name">Name of the article</div><div class="item__desc">Description of the article<span class="item__dots"></span>00.00</div></div>
    </div>

    <div class="feature" style="left:198px;top:62px">
      <div class="feature__title">Fresh &amp;<br>tasty</div>
      <p class="feature__text">Emotional description of the article or ingredients. A short note about taste, origin and how it is served.</p>
    </div>
    <div class="feature" style="left:198px;top:308px">
      <div class="feature__title">Unique pie</div>
      <p class="feature__text">Emotional description of the article or ingredients. A short note about taste, origin and how it is served.</p>
    </div>
  </section>

  <!-- Page: desserts & drinks -->
  <section class="page page--drinks">
    <div class="photo photo--platter" style="left:1px;top:2px;width:452px;height:276px" role="img" aria-label="Photo of a platter with cured ham, melon, pears and cheese"></div>
    <div class="feature" style="left:174px;top:216px">
      <div class="feature__title">A good end</div>
      <p class="feature__text">Emotional description of the article or ingredients. A short note about taste, origin and how it is served.</p>
    </div>

    <div class="section" style="left:70px;top:340px">
      <div class="section__head"><span class="marker"></span><span class="section__title">Desserts</span></div>
    </div>
    <div class="section" style="left:252px;top:340px">
      <div class="section__head" style="gap:72px"><span class="section__title">Drinks</span><span class="marker"></span></div>
    </div>
    <div class="items" style="left:94px;top:367px">
      <div class="item"><div class="item__name">Name of the article</div><div class="item__desc">Description of the article<span class="item__dots"></span>00.00</div></div>
      <div class="item"><div class="item__name">Name of the article</div><div class="item__desc">Description of the article<span class="item__dots"></span>00.00</div></div>
      <div class="item"><div class="item__name">Name of the article</div><div class="item__desc">Description of the article<span class="item__dots"></span>00.00</div></div>
      <div class="item"><div class="item__name">Name of the article</div><div class="item__desc">Description of the article<span class="item__dots"></span>00.00</div></div>
      <div class="item"><div class="item__name">Name of the article</div><div class="item__desc">Description of the article<span class="item__dots"></span>00.00</div></div>
    </div>
    <div class="items" style="left:252px;top:367px">
      <div class="item"><div class="item__name">Name of the article</div><div class="item__desc">Description of the article<span class="item__dots"></span>00.00</div></div>
      <div class="item"><div class="item__name">Name of the article</div><div class="item__desc">Description of the article<span class="item__dots"></span>00.00</div></div>
    </div>
    <span class="badge" style="left:43px;top:444px"><svg><use href="#i-leaf"/></svg></span>

    <div class="section" style="left:70px;top:512px">
      <div class="section__head"><span class="marker"></span><span class="section__title">Coffee</span></div>
    </div>
    <div class="items" style="left:94px;top:556px">
      <div class="item"><div class="item__name">Name of the article</div><div class="item__desc">Description of the article<span class="item__dots"></span>00.00</div></div>
      <div class="item"><div class="item__name">Name of the article</div><div class="item__desc">Description of the article<span class="item__dots"></span>00.00</div></div>
      <div class="item"><div class="item__name">Name of the article</div><div class="item__desc">Description of the article<span class="item__dots"></span>00.00</div></div>
      <div class="item"><div class="item__name">Name of the article</div><div class="item__desc">Description of the article<span class="item__dots"></span>00.00</div></div>
      <div class="item"><div class="item__name">Name of the article</div><div class="item__desc">Description of the article<span class="item__dots"></span>00.00</div></div>
    </div>
    <span class="badge" style="left:43px;top:558px"><svg><use href="#i-moon"/></svg></span>
    <span class="badge" style="left:43px;top:587px"><svg><use href="#i-moon"/></svg></span>
  </section>

  <!-- Page: main meals -->
  <section class="page page--meals">
    <div class="photo photo--beans" style="left:1px;top:0;width:230px;height:228px" role="img" aria-label="Photo of roasted coffee beans"></div>
    <div class="photo photo--salad" style="left:1px;top:232px;width:230px;height:244px" role="img" aria-label="Photo of a vegetable dish with cured ham and tomatoes"></div>
    <div class="photo photo--pasta" style="left:1px;top:482px;width:230px;height:226px" role="img" aria-label="Photo of spaghetti with olives and tomatoes"></div>

    <div class="feature" style="left:151px;top:60px">
      <div class="feature__title">Delicious!</div>
      <p class="feature__text">Emotional description of the article or ingredients. A short note about taste, origin and how it is served.</p>
    </div>
    <div class="feature" style="left:151px;top:301px">
      <div class="feature__title">Vegetal<br>hamburger</div>
      <p class="feature__text">Emotional description of the article or ingredients.</p>
    </div>
    <div class="feature" style="left:151px;top:548px">
      <div class="feature__title">Fresh meat</div>
      <p class="feature__text">Emotional description of the article or ingredients. A short note about taste, origin and how it is served.</p>
    </div>

    <div class="section" style="left:274px;top:23px">
      <div class="section__head"><span class="marker"></span><span class="section__title">Chicken meals</span></div>
    </div>
    <div class="items" style="left:300px;top:50px">
      <div class="item"><div class="item__name">Name of the article</div><div class="item__desc">Description of the article<span class="item__dots"></span>00.00</div></div>
      <div class="item"><div class="item__name">Name of the article</div><div class="item__desc">Description of the article<span class="item__dots"></span>00.00</div></div>
      <div class="item"><div class="item__name">Name of the article</div><div class="item__desc">Description of the article<span class="item__dots"></span>00.00</div></div>
      <div class="item"><div class="item__name">Name of the article</div><div class="item__desc">Description of the article<span class="item__dots"></span>00.00</div></div>
      <div class="item"><div class="item__name">Name of the article</div><div class="item__desc">Description of the article<span class="item__dots"></span>00.00</div></div>
      <div class="item"><div class="item__name">Name of the article</div><div class="item__desc">Description of the article<span class="item__dots"></span>00.00</div></div>
    </div>
    <span class="badge" style="left:274px;top:53px"><svg><use href="#i-star"/></svg></span>
    <span class="badge" style="left:274px;top:111px"><svg><use href="#i-flame"/></svg></span>

    <div class="section" style="left:274px;top:244px">
      <div class="section__head"><span class="marker"></span><span class="section__title">Hamburgers</span></div>
    </div>
    <div class="items" style="left:300px;top:270px">
      <div class="item"><div class="item__name">Name of the article</div><div class="item__desc">Description of the article<span class="item__dots"></span>00.00</div></div>
      <div class="item"><div class="item__name">Name of the article</div><div class="item__desc">Description of the article<span class="item__dots"></span>00.00</div></div>
      <div class="item"><div class="item__name">Name of the article</div><div class="item__desc">Description of the article<span class="item__dots"></span>00.00</div></div>
      <div class="item"><div class="item__name">Name of the article</div><div class="item__desc">Description of the article<span class="item__dots"></span>00.00</div></div>
      <div class="item"><div class="item__name">Name of the article</div><div class="item__desc">Description of the article<span class="item__dots"></span>00.00</div></div>
      <div class="item"><div class="item__name">Name of the article</div><div class="item__desc">Description of the article<span class="item__dots"></span>00.00</div></div>
      <div class="item"><div class="item__name">Name of the article</div><div class="item__desc">Description of the article<span class="item__dots"></span>00.00</div></div>
      <div class="item"><div class="item__name">Name of the article</div><div class="item__desc">Description of the article<span class="item__dots"></span>00.00</div></div>
    </div>
    <span class="badge" style="left:274px;top:302px"><svg><use href="#i-flower"/></svg></span>
    <span class="badge" style="left:274px;top:331px"><svg><use href="#i-flower"/></svg></span>
    <span class="badge" style="left:274px;top:389px"><svg><use href="#i-kid"/></svg></span>

    <div class="section" style="left:274px;top:512px">
      <div class="section__head"><span class="marker"></span><span class="section__title">Selected meat</span></div>
    </div>
    <div class="items" style="left:300px;top:538px">
      <div class="item"><div class="item__name">Name of the article</div><div class="item__desc">Description of the article<span class="item__dots"></span>00.00</div></div>
      <div class="item"><div class="item__name">Name of the article</div><div class="item__desc">Description of the article<span class="item__dots"></span>00.00</div></div>
      <div class="item"><div class="item__name">Name of the article</div><div class="item__desc">Description of the article<span class="item__dots"></span>00.00</div></div>
      <div class="item"><div class="item__name">Name of the article</div><div class="item__desc">Description of the article<span class="item__dots"></span>00.00</div></div>
      <div class="item"><div class="item__name">Name of the article</div><div class="item__desc">Description of the article<span class="item__dots"></span>00.00</div></div>
      <div class="item"><div class="item__name">Name of the article</div><div class="item__desc">Description of the article<span class="item__dots"></span>00.00</div></div>
    </div>
    <span class="badge" style="left:274px;top:599px"><svg><use href="#i-star"/></svg></span>
    <span class="badge" style="left:274px;top:686px"><svg><use href="#i-kid"/></svg></span>
  </section>

  <!-- Page: cover -->
  <section class="page page--cover">
    <div class="brand"><span class="brand__name">Bright<br>Corvella</span></div>
    <p class="welcome">Welcome to your restaurant name. Here you will find some of our recommendations that introduce ourselves in the fine art of generate sensations. Let us guide you trough this experience</p>

    <div class="thumb" style="left:18px"><div class="thumb__fill fill--pasta" role="img" aria-label="Photo of a pasta dish"></div></div>
    <div class="thumb" style="left:167px"><div class="thumb__fill fill--grill" role="img" aria-label="Photo of grilled meat"></div></div>
    <div class="thumb" style="left:316px"><div class="thumb__fill fill--chicken" role="img" aria-label="Photo of a roasted chicken dish"></div></div>

    <div class="section" style="left:18px;top:402px"><div class="section__head"><span class="section__title">Pasta</span></div></div>
    <div class="section" style="left:167px;top:402px"><div class="section__head"><span class="section__title">Grilled meat</span></div></div>
    <div class="section" style="left:316px;top:402px"><div class="section__head"><span class="section__title">Chicken</span></div></div>

    <div class="items" style="left:18px;top:426px">
      <div class="item"><div class="item__name">Name of the article</div><div class="item__desc">Description of the article<span class="item__dots"></span>00.00</div></div>
      <div class="item"><div class="item__name">Name of the article</div><div class="item__desc">Description of the article<span class="item__dots"></span>00.00</div></div>
      <div class="item"><div class="item__name">Name of the article</div><div class="item__desc">Description of the article<span class="item__dots"></span>00.00</div></div>
    </div>
    <div class="items" style="left:167px;top:426px">
      <div class="item"><div class="item__name">Name of the article</div><div class="item__desc">Description of the article<span class="item__dots"></span>00.00</div></div>
      <div class="item"><div class="item__name">Name of the article</div><div class="item__desc">Description of the article<span class="item__dots"></span>00.00</div></div>
      <div class="item"><div class="item__name">Name of the article</div><div class="item__desc">Description of the article<span class="item__dots"></span>00.00</div></div>
    </div>
    <div class="items" style="left:316px;top:426px">
      <div class="item"><div class="item__name">Name of the article</div><div class="item__desc">Description of the article<span class="item__dots"></span>00.00</div></div>
      <div class="item"><div class="item__name">Name of the article</div><div class="item__desc">Description of the article<span class="item__dots"></span>00.00</div></div>
      <div class="item"><div class="item__name">Name of the article</div><div class="item__desc">Description of the article<span class="item__dots"></span>00.00</div></div>
    </div>
    <span class="badge" style="left:145px;top:459px"><svg><use href="#i-star"/></svg></span>
    <span class="badge" style="left:294px;top:430px"><svg><use href="#i-star"/></svg></span>
    <span class="badge" style="left:294px;top:459px"><svg><use href="#i-star"/></svg></span>

    <footer class="cover__footer">
      <div class="symbols__head">
        <span class="marker"></span>
        <div class="symbols__title">Symbols</div>
        <div class="symbols__sub">This will help you choose...</div>
      </div>
      <div class="symbol" style="left:70px"><span class="badge"><svg><use href="#i-star"/></svg></span><div class="symbol__name">TOP FLAVOUR</div><div class="symbol__text">You have to try this one</div></div>
      <div class="symbol" style="left:122px"><span class="badge"><svg><use href="#i-flame"/></svg></span><div class="symbol__name">SPICY</div><div class="symbol__text">For the intense taste lovers</div></div>
      <div class="symbol" style="left:175px"><span class="badge"><svg><use href="#i-flower"/></svg></span><div class="symbol__name">VEGETAL</div><div class="symbol__text">Just vegetables no more no less</div></div>
      <div class="symbol" style="left:227px"><span class="badge"><svg><use href="#i-leaf"/></svg></span><div class="symbol__name">FAT FREE</div><div class="symbol__text">Nice meal with low calories</div></div>
      <div class="symbol" style="left:280px"><span class="badge"><svg><use href="#i-zero"/></svg></span><div class="symbol__name">NO ALCOHOL</div><div class="symbol__text">No alcohol drinks</div></div>
      <div class="symbol" style="left:331px"><span class="badge"><svg><use href="#i-moon"/></svg></span><div class="symbol__name">NO CAFFEINE</div><div class="symbol__text">No caffeine drinks</div></div>
      <div class="symbol" style="left:384px"><span class="badge"><svg><use href="#i-kid"/></svg></span><div class="symbol__name">KIDS</div><div class="symbol__text">Special meal for kids</div></div>
    </footer>
  </section>

</main>
</body>
</html>
```